Business Card Design

Needing a business card design similar to the business card that is attached.

Industry/Entity Type

Business

Contact Information for Business Card

Design similar to the b-cards that is attached.

```html
<!DOCTYPE html>
<html lang="en">
<head>
<meta charset="utf-8">
<title>Business Cards</title>
<link rel="stylesheet" href="https://fonts.googleapis.com/css2?family=Oswald:wght@600&family=Exo+2:wght@700&family=PT+Serif:wght@400;700&display=swap">
<style>
  :root {
    --backdrop: #e9e6e1;
    --card: #ffffff;
    --ink: #1d1d1d;
    --realty-blue: #1e8fe0;
    --realty-band: #5dbef2;
    --realty-mark: #1b7fcc;
    --solar-green: #1f9a45;
    --solar-band: #6cc43c;
    --solar-mark: #2e9d3f;
  }
  * { box-sizing: border-box; margin: 0; padding: 0; }
  html, body { width: 1200px; height: 900px; overflow: hidden; }
  body {
    background: var(--backdrop);
    position: relative;
    font-family: "PT Serif", Georgia, serif;
    color: var(--ink);
  }
  .card {
    position: absolute;
    left: 278px;
    width: 640px;
    height: 375px;
    background: var(--card);
    box-shadow: 0 4px 14px rgba(0,0,0,0.25);
    overflow: hidden;
  }
  .card--realty { top: 65px; }
  .card--solar { top: 463px; }
  .brand {
    position: absolute;
    display: flex;
    align-items: center;
    white-space: nowrap;
  }
  .card--realty .brand { left: 80px; top: 43px; gap: 22px; }
  .card--solar .brand { left: 74px; top: 34px; gap: 10px; }
  .brand-mark { display: block; flex: none; }
  .brand-name--realty {
    font-family: "Oswald", "Arial Narrow", sans-serif;
    font-weight: 600;
    font-size: 41px;
    letter-spacing: 0.5px;
    color: var(--ink);
  }
  .brand-name--solar {
    font-family: "Exo 2", Arial, sans-serif;
    font-weight: 700;
    font-size: 44px;
    color: var(--solar-green);
  }
  .person {
    position: absolute;
    left: 0; right: 0;
    top: 160px;
    text-align: center;
  }
  .person-name { font-size: 24px; line-height: 28px; }
  .card--realty .person-name { color: var(--realty-blue); }
  .card--solar .person-name { color: var(--solar-green); }
  .person-role { font-size: 16px; font-weight: 700; line-height: 22px; }
  .contact-band {
    position: absolute;
    left: 0; right: 0; bottom: 0;
    height: 93px;
    padding-top: 10px;
    text-align: center;
    font-size: 15px;
    line-height: 23px;
  }
  .card--realty .contact-band { background: var(--realty-band); }
  .card--solar .contact-band { background: var(--solar-band); }
  .gap { display: inline-block; width: 18px; }
</style>
</head>
<body>
  <section class="card card--realty">
    <div class="brand">
      <svg class="brand-mark" width="108" height="70" viewBox="0 0 108 70" aria-hidden="true">
        <rect x="19" y="0" width="70" height="70" rx="10" fill="var(--realty-mark)"/>
      </svg>
      <span class="brand-name--realty">HARBOR REALTY, INC.</span>
    </div>
    <div class="person">
      <p class="person-name">Daniel Okafor</p>
      <p class="person-role">Managing Broker</p>
    </div>
    <div class="contact-band">
      <p>4820 S 212th St. # B200, Auburn, WA 98001</p>
      <p>P: (206) 555-0148<span class="gap"></span>F: (253) 555-0172</p>
      <p>www.harborrealtyinc.com</p>
    </div>
  </section>

  <section class="card card--solar">
    <div class="brand">
      <svg class="brand-mark" width="80" height="80" viewBox="0 0 80 80" aria-hidden="true">
        <circle cx="40" cy="40" r="38" fill="var(--solar-mark)"/>
      </svg>
      <span class="brand-name--solar">CascadeTherm, Inc.</span>
    </div>
    <div class="person">
      <p class="person-name">Daniel Okafor</p>
      <p class="person-role">M. E. &amp; Certified Geothermal Installer</p>
    </div>
    <div class="contact-band">
      <p>4820 S 212th St. # B200, Auburn, WA 98001</p>
      <p>P: (206) 555-0148</p>
      <p>www.harborrealtyinc.com</p>
    </div>
  </section>
</body>
</html>
```